Healthy lifestyle Influencer business card

I need your creativity to have a business card that I can leave in all the restaurants, hotels and spas I visit to inform them that I am an influencer specializing in the wellness sector and that I will write a review about them. You can use my instagram photos Lunavivo27 or on my website www.piattileggerisani.it. I would like my business card to impress with its creativity! thank you very much!

Contact Information for Business Card

siteweb, instagram, phone number

Font styles to use
Decorative
Script

Colors
0094D4
00A9DD
6FCCEA
C7EBF8
E9F6FB
59FF00
82FF00
B8FF75
E3FFCB
F4FFEA
FFC000
F8CF3A
FAE287
FDF2CF
FEFAEE
F0912C
F2A743
F7CA91
FBE8D2
FDF5EE
EE7325
F08F49
F5BC92
FAE3D3
FDF4ED
EB3D1F
EC4F4E
F09395
F8D3D4
FCEDEE
E54698
E96AAD
F1A4CE
F9D9EA
FCEFF6

Requirements
Nice to have
• creativity

```html
<!DOCTYPE html>
<html lang="it">
<head>
<meta charset="utf-8">
<title>Luna Leggera – Biglietto da visita</title>
<link href="https://fonts.googleapis.com/css2?family=Montserrat:wght@500&family=Marck+Script&family=Cormorant+Garamond:wght@500&display=swap" rel="stylesheet">
<style>
  :root {
    --bg: #e4e4e6;
    --card: #ffffff;
    --card-shade: #f1f1f3;
    --mint: #97b8ad;
    --ink: #5d5d60;
    --ink-dark: #4a4a4d;
    --photo-light: #f4f4f5;
    --photo-mid: #cfd0d2;
    --photo-dark: #a9aaad;
  }
  * { box-sizing: border-box; margin: 0; padding: 0; }
  html, body { width: 1200px; height: 1024px; overflow: hidden; }
  body {
    background: var(--bg);
    display: flex;
    flex-direction: column;
    align-items: center;
    justify-content: center;
    gap: 44px;
    font-family: "Montserrat", sans-serif;
  }
  .card {
    position: relative;
    width: 790px;
    height: 451px;
    background: linear-gradient(160deg, var(--card) 0%, var(--card-shade) 100%);
    box-shadow: 0 6px 18px rgba(0,0,0,0.18);
    overflow: hidden;
  }

  /* front */
  .brand {
    position: absolute;
    top: 62px;
    left: 0; right: 0;
    text-align: center;
  }
  .brand-name {
    font-family: "Montserrat", sans-serif;
    font-weight: 500;
    font-size: 46px;
    line-height: 1.15;
    color: var(--ink);
    letter-spacing: 1px;
  }
  .brand-tagline {
    margin-top: 6px;
    font-size: 17px;
    font-weight: 500;
    color: var(--ink);
  }
  .band {
    position: absolute;
    left: 0; right: 0;
    background: var(--mint);
  }
  .band-top { top: 186px; height: 14px; }
  .person-name {
    position: absolute;
    top: 218px;
    left: 0; right: 0;
    text-align: center;
    font-family: "Marck Script", cursive;
    font-size: 46px;
    line-height: 1.1;
    color: var(--ink-dark);
  }
  .band-contacts {
    top: 292px;
    height: 34px;
    display: flex;
    align-items: center;
    justify-content: center;
    gap: 26px;
    color: #ffffff;
    font-size: 16px;
    font-weight: 500;
  }
  .contact { display: flex; align-items: center; gap: 7px; }
  .contact svg { display: block; }
  .website {
    position: absolute;
    top: 346px;
    left: 0; right: 0;
    text-align: center;
    font-family: "Cormorant Garamond", serif;
    font-size: 20px;
    font-weight: 500;
    letter-spacing: 7px;
    color: var(--ink);
  }
  .band-bottom { top: 396px; height: 22px; }

  /* back */
  .card-back { background: var(--card); }
  .back-photo {
    position: absolute;
    inset: 0;
    background:
      linear-gradient(180deg, rgba(255,255,255,0) 35%, var(--photo-light) 92%),
      linear-gradient(180deg, var(--photo-mid) 0%, var(--photo-dark) 38%, var(--photo-mid) 55%, var(--photo-light) 100%);
  }
  .back-brand {
    position: absolute;
    top: 170px;
    left: 0; right: 0;
    text-align: center;
  }
  .back-brand .brand-name { font-size: 34px; }
  .back-brand .brand-tagline { font-size: 13px; margin-top: 4px; }
</style>
</head>
<body>

<section class="card card-front">
  <div class="brand">
    <div class="brand-name">Luna Leggera</div>
    <div class="brand-tagline">Leggeri e felici a tavola</div>
  </div>
  <div class="band band-top"></div>
  <div class="person-name">Luna Vivaldi Serrani</div>
  <div class="band band-contacts">
    <span class="contact">
      <svg width="16" height="14" viewBox="0 0 16 14" aria-hidden="true">
        <path d="M1 4 Q8 -1 15 4 L13 6 L11 4.5 L5 4.5 L3 6 Z" fill="#fff"/>
        <rect x="3" y="7" width="10" height="6" rx="1.5" fill="#fff"/>
      </svg>
      123-555-0147
    </span>
    <span class="contact">
      <svg width="14" height="14" viewBox="0 0 14 14" aria-hidden="true">
        <circle cx="7" cy="7" r="6" fill="none" stroke="#fff" stroke-width="1.6"/>
      </svg>
      Lunavivo27
    </span>
  </div>
  <div class="website">www.piattileggerisani.it</div>
  <div class="band band-bottom"></div>
</section>

<section class="card card-back">
  <div class="back-photo" role="img" aria-label="Foto in bianco e nero di due donne che scuotono i capelli bagnati in mare, con bungalow sull'acqua sullo sfondo"></div>
  <div class="back-brand">
    <div class="brand-name">Luna Leggera</div>
    <div class="brand-tagline">Leggeri e felici a tavola</div>
  </div>
</section>

</body>
</html>
```